DL Flyer Design

I need a DL flyer, double-sided designed for a Brisbane based outdoor group exercise/training company called Step Up! Step Up! provides group outdoor training, designed for the individual. It provides the support, motivation and one-on-one attention of personal training combined with the support of a group environment. The classes are fun, challenging and aim to develop confidence & fitness. Weight loss is not the focus, although it is a benefit.
Updates

Hi

I've just uploaded a high res version of the logo if you need.

Cheers
Tam

Target Market(s)

English speaking men & women aged 25 - 45, white-collar office jobs. Average-low level of fitness, not hugely 'fitness' oriented but want to improve quality of life, overall fitness, lose a bit of weight.

Computer and consumer literate. Live in suburban Brisbane, Australia.

Industry/Entity Type

Training

Requirements
Must have
• Double sided DL. Use of black, greens and white per attached photos. Use of 1300 572 914 (1300 STEP UP) and website www.stepupactive.example.au

Indicative copy and contents is posted in the comments section.

```html
<!DOCTYPE html>
<html lang="en">
<head>
<meta charset="utf-8">
<title>Step Up! DL Flyer</title>
<link rel="stylesheet" href="https://fonts.googleapis.com/css2?family=Archivo:wght@700;800;900&family=Arimo:wght@400;700&display=swap">
<style>
  :root {
    --stage: #333333;
    --paper: #ffffff;
    --ink: #1e1e1e;
    --green: #3daa35;
    --green-light: #8cc63f;
    --green-pale: #eef6e4;
    --green-row: #b9dd8c;
    --green-head: #5bb947;
    --muted: #555555;
  }
  * { box-sizing: border-box; margin: 0; padding: 0; }
  html, body { width: 1200px; height: 900px; overflow: hidden; background: var(--stage); }
  body { position: relative; font-family: "Arimo", Arial, sans-serif; color: var(--ink); }
  .panel {
    position: absolute; top: 8px; width: 440px; height: 880px;
    background: var(--paper); overflow: hidden;
  }
  .panel--front { left: 156px; }
  .panel--back { left: 608px; }
  .panel > * { z-index: 1; }
  .figure-wash {
    position: absolute; z-index: 0; border-radius: 48% 52% 40% 60%;
    background: radial-gradient(ellipse at center, var(--green-pale) 0%, rgba(238,246,228,0) 72%);
  }
  .figure-small {
    position: absolute; z-index: 2; width: 64px; height: 84px; border-radius: 40% 40% 20% 20%;
    background: linear-gradient(180deg, var(--green-light), var(--green));
    opacity: .6;
  }
  .wordmark {
    position: absolute; font-family: "Archivo", Arial, sans-serif; font-weight: 900;
    color: var(--green); letter-spacing: -1px; line-height: 1;
  }
  .panel--front .wordmark { top: 48px; left: 0; width: 100%; text-align: center; font-size: 64px; }
  .panel--back .wordmark { top: 36px; left: 28px; font-size: 46px; }
  .head {
    font-family: "Archivo", Arial, sans-serif; font-weight: 800; line-height: 1.15;
  }
  .intro { position: absolute; top: 184px; left: 0; width: 100%; text-align: center; font-size: 27px; }
  .intro .big { color: var(--green); font-size: 46px; line-height: 1.05; margin-top: 12px; }
  .intro .big .you { color: var(--green-light); }
  .body-copy { position: absolute; top: 390px; left: 44px; width: 360px; font-size: 16px; line-height: 1.3; }
  .body-copy p { margin-bottom: 26px; }
  .body-copy .brand { color: var(--green); font-weight: 700; }
  .body-copy .note { color: var(--green); }
  .front-call { position: absolute; top: 650px; left: 44px; }
  .front-call .label { font-size: 20px; }
  .front-call .number { color: var(--green); font-size: 24px; }
  .tagline { position: absolute; top: 716px; left: 40px; width: 370px; font-size: 27px; line-height: 1.1; }
  .tagline .line2 { text-align: right; }
  .tagline .accent { color: var(--green); }
  .url-band {
    position: absolute; left: 0; bottom: 0; width: 100%; height: 48px;
    background: var(--green); color: var(--paper); font-size: 15px;
    padding: 14px 0 0 44px;
  }
  .back-call { position: absolute; top: 160px; left: 28px; }
  .back-call .label { font-size: 28px; }
  .back-call .number { color: var(--green); font-size: 42px; line-height: 1.1; margin-top: 8px; }
  .back-call .number .alt { color: var(--green-light); }
  .back-call .url { font-family: "Archivo", Arial, sans-serif; font-weight: 700; font-size: 20px; margin-top: 10px; }
  .back-call .location { font-size: 12px; color: var(--muted); margin-top: 12px; }
  .program { position: absolute; top: 412px; left: 26px; width: 390px; }
  .program h2 { font-size: 18px; margin-bottom: 6px; }
  .schedule { width: 100%; border-collapse: separate; border-spacing: 2px; font-size: 9px; text-align: center; }
  .schedule th { background: var(--green-head); color: var(--ink); height: 16px; font-weight: 700; }
  .schedule td { background: var(--green-row); height: 38px; line-height: 1.2; }
  .schedule td.time { font-weight: 700; }
</style>
</head>
<body>

<section class="panel panel--front">
  <div class="figure-wash" style="left:-20px;top:340px;width:420px;height:500px" role="img" aria-label="Faint silhouette of a leaping runner"></div>
  <div class="wordmark">Step Up!</div>
  <div class="head intro">
    <div>It's time to Step Up!<br>with group outdoor training,</div>
    <div class="big">designed<br>just for <span class="you">you.</span></div>
  </div>
  <div class="body-copy">
    <p><span class="brand">Step Up!</span> provides the unique combination of the one-on-one attention of personal training with the motivation and support of a group environment.</p>
    <p>Best of all, it's designed to fit fitness into your life - at an affordable price.</p>
    <p>Curious? Give it a shot with a 1 week free trial!</p>
    <p class="note">(Guaranteed no hard sell at the end)</p>
  </div>
  <div class="head front-call">
    <div class="label">Call Now :</div>
    <div class="number">1300 572 914 (1300 STEP UP)</div>
  </div>
  <div class="head tagline">
    <div>Tired of hanging about?</div>
    <div class="line2">.....Just <span class="accent">Step Up!</span></div>
  </div>
  <div class="url-band">www.stepupactive.example.au</div>
  <div class="figure-small" style="left:352px;top:792px" role="img" aria-label="Small green silhouette of a runner"></div>
</section>

<section class="panel panel--back">
  <div class="figure-wash" style="left:0;top:360px;width:430px;height:480px" role="img" aria-label="Faint silhouette of a leaping runner"></div>
  <div class="wordmark">Step Up!</div>
  <div class="head back-call">
    <div class="label">Call Now :</div>
    <div class="number">1300 572 914<br><span class="alt">(1300 STEP UP)</span></div>
    <div class="url">www.stepupactive.example.au</div>
    <div class="location">Location: (**details not confirmed)</div>
  </div>
  <div class="program">
    <h2 class="head">Session Program:</h2>
    <table class="schedule">
      <tr><th>Time</th><th>Monday</th><th>Tuesday</th><th>Wednesday</th><th>Thursday</th><th>Friday</th><th>Saturday</th></tr>
      <tr><td class="time">6:00 am</td><td>Cardio</td><td>-</td><td>Boxing circuit</td><td>Cardio</td><td>Boxing circuit</td><td>Mash up</td></tr>
      <tr><td></td><td></td><td></td><td></td><td></td><td></td><td>One on One Sessions</td></tr>
      <tr><td class="time">6:00 pm</td><td>Strength</td><td>Cardio</td><td>Strength</td><td>Boxing circuit</td><td></td><td></td></tr>
    </table>
  </div>
  <div class="figure-small" style="left:346px;top:792px" role="img" aria-label="Small green silhouette of a runner"></div>
</section>

</body>
</html>
```